Business card design for new, innovative company - BoldHarbor

We are a new company looking for a business card design that is fun, different and quirky. Must use corporate colour green - CMYK C:55, M:0, Y:100, K:0, and corporate colour grey - C:0, M:0, Y: 0, K:70.

We have developed the first real time data application, in which people are able to profile the data of their existing customers in order to pull out more good fit clients to direct their marketing activities at.

Industry/Entity Type

Marketing

Requirements
Must have
• Logo, name, title, telephone number, fax number, email, website, address

```html
<!DOCTYPE html>
<html lang="en">
<head>
<meta charset="utf-8">
<title>BoldHarbor business cards</title>
<link rel="stylesheet" href="https://fonts.googleapis.com/css2?family=Open+Sans:ital,wght@0,400;0,600;0,700;1,400&display=swap">
<style>
  :root {
    --brand-green: #7dc242;
    --brand-grey: #6d6e71;
    --tab-grey: #707173;
    --text-grey: #58595b;
    --board-light: #fbfbfb;
    --board-edge: #e4e4e4;
    --card-white: #ffffff;
  }
  html, body {
    margin: 0; padding: 0;
    width: 1200px; height: 1200px;
    overflow: hidden;
  }
  body {
    font-family: "Open Sans", Arial, sans-serif;
    background: radial-gradient(ellipse at 50% 40%, var(--board-light) 30%, var(--board-edge) 100%);
    position: relative;
  }
  .card {
    position: absolute;
    width: 528px; height: 300px;
    overflow: hidden;
    box-shadow: 3px 4px 8px rgba(0,0,0,0.35);
    background: var(--card-white);
  }
  .card--male { left: 326px; top: 160px; }
  .card--female { left: 90px; top: 488px; }
  .card--back { left: 598px; top: 554px; }

  .photo { position: absolute; inset: 0; }
  .photo--shirt-tie {
    background:
      linear-gradient(90deg, transparent 0 19%, #8cc43c 19% 41%, transparent 41%),
      linear-gradient(180deg, #f2f2f2, #dcdcdc);
  }
  .photo--vest {
    background:
      linear-gradient(160deg, #e9e9ef 0 22%, transparent 22%),
      linear-gradient(135deg, #8fc742, #6fae2e 70%, #5e9a25);
  }
  .url-tab {
    position: absolute;
    left: 276px; top: 0;
    width: 194px; height: 47px;
    background: var(--tab-grey);
    color: #fff;
    font-weight: 700; font-size: 16px;
    display: flex; align-items: center; justify-content: center;
  }
  .card--female .url-tab { left: 278px; }
  .wordmark {
    position: absolute;
    font-weight: 700;
    font-size: 31px;
    letter-spacing: -1px;
    line-height: 1;
  }
  .card--male .wordmark { left: 274px; top: 212px; color: var(--brand-grey); }
  .card--female .wordmark { left: 276px; top: 212px; color: #fff; }

  .back-bar {
    position: absolute; left: 56px; top: 0;
    width: 194px; height: 34px;
    background: var(--brand-green);
  }
  .card--back .wordmark { left: 56px; top: 42px; color: var(--brand-grey); }
  .contact {
    position: absolute; right: 44px; top: 84px;
    text-align: right; color: var(--text-grey);
  }
  .contact__name { font-size: 19px; font-weight: 600; margin: 0; color: var(--text-grey); }
  .contact__title { font-size: 15px; font-style: italic; margin: 0 0 12px; }
  .contact__row {
    display: flex; justify-content: flex-end; align-items: flex-start;
    gap: 8px; font-size: 15px; line-height: 20px; margin-bottom: 6px;
  }
  .contact__icon { width: 22px; height: 22px; flex: none; }
  .back-url {
    position: absolute; left: 56px; bottom: 18px;
    color: var(--brand-green); font-weight: 700; font-size: 17px;
  }

  .footer-band {
    position: absolute; left: 6px; top: 1032px;
    width: 1188px; height: 162px;
    background: var(--brand-green);
  }
  .footer-band .wordmark {
    left: 66px; top: 52px; color: #fff; font-size: 50px; letter-spacing: -2px;
  }
  .legend-box {
    position: absolute;
    border: 1.5px solid #fff;
    box-sizing: border-box;
    color: #fff; font-size: 13px;
    padding: 0 6px 2px;
    display: flex; align-items: flex-end;
  }
  .legend-box--male { left: 967px; top: 16px; width: 105px; height: 57px; }
  .legend-box--female { left: 924px; top: 79px; width: 105px; height: 59px; background: var(--brand-green); }
  .legend-box--back { left: 1024px; top: 92px; width: 104px; height: 59px; justify-content: flex-end; background: var(--brand-green); }
</style>
</head>
<body>
  <section class="card card--male">
    <div class="photo photo--shirt-tie" role="img" aria-label="Photo of a white shirt with a green tie"></div>
    <div class="url-tab">www.boldharbor.com</div>
    <div class="wordmark">BoldHarbor</div>
  </section>

  <section class="card card--female">
    <div class="photo photo--vest" role="img" aria-label="Photo of a green waistcoat over a white blouse"></div>
    <div class="url-tab">www.boldharbor.com</div>
    <div class="wordmark">BoldHarbor</div>
  </section>

  <section class="card card--back">
    <div class="back-bar"></div>
    <div class="wordmark">BoldHarbor</div>
    <div class="contact">
      <p class="contact__name">Clara Benton</p>
      <p class="contact__title">title of person</p>
      <div class="contact__row"><span>070 1234 5678</span>
        <svg class="contact__icon" viewBox="0 0 22 22"><rect width="22" height="22" rx="5" fill="var(--brand-grey)"/><rect x="7" y="3" width="8" height="16" rx="1.5" fill="#fff"/><rect x="8.5" y="5" width="5" height="6" fill="var(--brand-grey)"/></svg></div>
      <div class="contact__row"><span>012 3456 7890</span>
        <svg class="contact__icon" viewBox="0 0 22 22"><rect width="22" height="22" rx="5" fill="var(--brand-grey)"/><path d="M6 4c-2 2 0 7 4 11s8 5 9 3l-3-3-2 1c-2-1-4-3-5-5l1-2z" fill="#fff"/></svg></div>
      <div class="contact__row"><span>clara.benton@boldharbor.com</span>
        <svg class="contact__icon" viewBox="0 0 22 22"><rect width="22" height="22" rx="5" fill="var(--brand-grey)"/><rect x="3.5" y="6" width="15" height="10" fill="none" stroke="#fff" stroke-width="1.6"/><path d="M3.5 6l7.5 6 7.5-6" fill="none" stroke="#fff" stroke-width="1.6"/></svg></div>
      <div class="contact__row"><span>22a Elmfield Road, Ashby,<br>Northshire, AB12 3CD</span>
        <svg class="contact__icon" viewBox="0 0 22 22"><rect width="22" height="22" rx="5" fill="var(--brand-grey)"/><path d="M4 11l7-6 7 6v7h-5v-4h-4v4H4z" fill="#fff"/></svg></div>
    </div>
    <div class="back-url">www.boldharbor.com</div>
  </section>

  <footer class="footer-band">
    <div class="wordmark">BoldHarbor</div>
    <div class="legend-box legend-box--male">Male</div>
    <div class="legend-box legend-box--female">Female</div>
    <div class="legend-box legend-box--back">Back</div>
  </footer>
</body>
</html>
```